Plivoro ( A new twist on task management )

We need modern, elegant, and clean (Material Design) on screens, buttons, and icons.

It is a (smart) task management application which helps the users to get notified and track task completion hassle free; Using notification profiles they create.

The interface of this application should be very simple and color schemes should be contemporary as long as they don’t make reading short text hard.

Following Material Design guidelines, the prefered font style is Roboto
Updates

Target Market(s)

Everyone from 13+

Industry/Entity Type

Software

Logo Text

Plivoro

Font styles to use
Other font styles liked:
• Roboto

```html
<!DOCTYPE html>
<html lang="en">
<head>
<meta charset="utf-8">
<title>Plivoro – New Profile, Repeat Every</title>
<link rel="stylesheet" href="https://fonts.googleapis.com/css2?family=Roboto:wght@400;500&display=swap">
<style>
  :root {
    --teal-dark: #00838f;
    --teal: #00a3b3;
    --teal-accent: #26bfd3;
    --tab-indicator: #ffe44d;
    --surface: #eeeeee;
    --surface-header: #fafafa;
    --field-grey: #d8d8d8;
    --text-strong: #333333;
    --text-muted: #6d6d6d;
    --line: #bdbdbd;
    --toggle-green: #2e9b3a;
    --fab-grey: #9e9e9e;
    --scrim: rgba(0, 0, 0, 0.54);
    --dialog: #ffffff;
    --dialog-title: #555555;
    --dialog-option: #6b6b6b;
    --dialog-divider: #e0e0e0;
    --radio-off: #9a9a9a;
    --nav-bar: #000000;
    --nav-icon: #cfcfcf;
  }
  * { box-sizing: border-box; margin: 0; padding: 0; }
  html, body { width: 675px; height: 1200px; overflow: hidden; }
  body { font-family: "Roboto", sans-serif; background: var(--surface); position: relative; }
  .abs { position: absolute; }

  .status-bar { left: 0; top: 0; width: 675px; height: 45px; background: var(--teal-dark); }
  .status-bar svg { position: absolute; left: 515px; top: 10px; }
  .status-time { right: 14px; top: 11px; font-size: 19px; color: #fff; }

  .app-bar { left: 0; top: 45px; width: 675px; height: 150px; background: var(--teal); }
  .avatar { left: 24px; top: 16px; width: 60px; height: 60px; border-radius: 50%; background: var(--teal-dark); }
  .profile-name { left: 103px; top: 30px; font-size: 24px; color: #fff; }
  .filter-icon { left: 613px; top: 28px; }
  .tab { top: 108px; width: 337px; text-align: center; font-size: 19px; font-weight: 500; letter-spacing: 0.6px; }
  .tab-tasks { left: 0; color: #fff; }
  .tab-profiles { left: 338px; color: rgba(255,255,255,0.7); }
  .tab-indicator { left: 337px; top: 147px; width: 338px; height: 3px; background: var(--tab-indicator); }

  .screen-title { left: 0; top: 195px; width: 675px; height: 72px; background: var(--surface-header);
    text-align: center; line-height: 72px; font-size: 24px; color: var(--text-strong); }

  .field-label { font-size: 23px; color: var(--text-muted); left: 24px; }
  .small-label { font-size: 19px; color: var(--text-strong); left: 24px; }
  .row-label { font-size: 24px; color: var(--text-strong); left: 24px; }
  .underline { height: 1px; background: var(--line); }
  .chevron { left: 636px; }

  .choice-box { left: 24px; top: 455px; width: 336px; height: 63px; background: var(--field-grey); }
  .choice-button { left: 360px; top: 455px; width: 289px; height: 63px; background: var(--teal); }

  .toggle-track { left: 591px; top: 569px; width: 50px; height: 14px; border-radius: 7px; background: #7fcf86; }
  .toggle-thumb { left: 622px; top: 562px; width: 28px; height: 28px; border-radius: 50%; background: var(--toggle-green); }

  .fab { width: 76px; height: 76px; border-radius: 50%; top: 1007px; }
  .fab svg { position: absolute; left: 26px; top: 26px; }
  .fab-cancel { left: 241px; background: var(--fab-grey); }
  .fab-confirm { left: 358px; background: var(--teal); }

  .scrim { left: 0; top: 0; width: 675px; height: 1109px; background: var(--scrim); }

  .nav-bar { left: 0; top: 1109px; width: 675px; height: 91px; background: var(--nav-bar); }
  .nav-bar svg { position: absolute; top: 27px; }

  .dialog { left: 99px; top: 325px; width: 478px; height: 442px; background: var(--dialog);
    border-radius: 3px; box-shadow: 0 10px 30px rgba(0,0,0,0.35); }
  .dialog-title { left: 30px; top: 27px; font-size: 22px; font-weight: 500; color: var(--dialog-title); }
  .dialog-divider { left: 0; width: 478px; height: 1px; background: var(--dialog-divider); }
  .option { left: 32px; height: 30px; display: flex; align-items: center; }
  .radio { width: 19px; height: 19px; border-radius: 50%; border: 2px solid var(--radio-off); position: relative; }
  .radio.is-checked { border-color: var(--teal-accent); }
  .radio.is-checked::after { content: ""; position: absolute; left: 3px; top: 3px; width: 9px; height: 9px;
    border-radius: 50%; background: var(--teal-accent); }
  .option-label { margin-left: 27px; font-size: 23px; color: var(--dialog-option); }
  .dialog-action { top: 392px; font-size: 19px; font-weight: 500; letter-spacing: 1px; color: var(--teal-accent); }
</style>
</head>
<body>
  <header class="status-bar abs">
    <svg width="70" height="24" viewBox="0 0 70 24">
      <path d="M0 4 Q13 -4 26 4 L13 21 Z" fill="#fff"/>
      <path d="M30 21 L48 3 L48 21 Z" fill="#fff"/>
      <rect x="55" y="2" width="11" height="20" rx="1" fill="#fff"/>
    </svg>
    <span class="status-time abs">12:30</span>
  </header>

  <div class="app-bar abs">
    <div class="avatar abs">
      <svg width="60" height="60" viewBox="0 0 60 60">
        <circle cx="28" cy="23" r="8" fill="#00b8c8"/>
        <path d="M14 44 Q14 33 28 33 Q42 33 42 44 Z" fill="#00b8c8"/>
        <path d="M41 41 h8 M45 37 v8" stroke="#00b8c8" stroke-width="2.5"/>
      </svg>
    </div>
    <span class="profile-name abs">Unknown</span>
    <svg class="filter-icon abs" width="38" height="34" viewBox="0 0 38 34" fill="none" stroke="#fff" stroke-width="2">
      <path d="M1 5 H37 M1 17 H37 M1 29 H37"/>
      <circle cx="24" cy="5" r="3.5" fill="#00a3b3"/>
      <circle cx="14" cy="17" r="3.5" fill="#00a3b3"/>
      <circle cx="24" cy="29" r="3.5" fill="#00a3b3"/>
    </svg>
    <span class="tab tab-tasks abs">TASKS</span>
    <span class="tab tab-profiles abs">PROFILES</span>
    <div class="tab-indicator abs"></div>
  </div>

  <main>
    <div class="screen-title abs">New Profile</div>

    <span class="field-label abs" style="top:322px">Enter Profile Name</span>
    <div class="underline abs" style="left:24px;top:365px;width:625px"></div>

    <span class="small-label abs" style="top:416px">Choose Notification Type</span>
    <div class="choice-box abs"></div>
    <div class="choice-button abs"></div>

    <span class="row-label abs" style="top:561px">Time Tracking</span>
    <div class="toggle-track abs"></div>
    <div class="toggle-thumb abs"></div>

    <span class="row-label abs" style="top:623px">Set Start Time</span>
    <svg class="chevron abs" style="top:628px" width="14" height="20" viewBox="0 0 14 20"><path d="M2 1 L11 10 L2 19" fill="none" stroke="#888" stroke-width="2"/></svg>

    <span class="row-label abs" style="top:685px">Repeat</span>
    <svg class="chevron abs" style="top:690px" width="14" height="20" viewBox="0 0 14 20"><path d="M2 1 L11 10 L2 19" fill="none" stroke="#888" stroke-width="2"/></svg>

    <span class="row-label abs" style="top:749px">Between</span>
    <div class="underline abs" style="left:191px;top:790px;width:203px"></div>
    <span class="row-label abs" style="left:414px;top:749px">to</span>
    <div class="underline abs" style="left:446px;top:790px;width:203px"></div>

    <div class="fab fab-cancel abs">
      <svg width="24" height="24" viewBox="0 0 24 24"><path d="M3 3 L21 21 M21 3 L3 21" stroke="#e0e0e0" stroke-width="2"/></svg>
    </div>
    <div class="fab fab-confirm abs">
      <svg width="24" height="24" viewBox="0 0 24 24"><path d="M3 13 L9 19 L21 6" fill="none" stroke="#e8f9fb" stroke-width="2"/></svg>
    </div>
  </main>

  <div class="scrim abs"></div>

  <nav class="nav-bar abs">
    <svg style="left:132px" width="36" height="36" viewBox="0 0 36 36"><path d="M30 3 L4 18 L30 33 Z" fill="none" stroke="var(--nav-icon)" stroke-width="3" stroke-linejoin="round"/></svg>
    <svg style="left:320px" width="36" height="36" viewBox="0 0 36 36"><circle cx="18" cy="18" r="15" fill="none" stroke="var(--nav-icon)" stroke-width="3"/></svg>
    <svg style="left:507px" width="36" height="36" viewBox="0 0 36 36"><rect x="4" y="4" width="28" height="28" fill="none" stroke="var(--nav-icon)" stroke-width="3"/></svg>
  </nav>

  <section class="dialog abs" role="dialog" aria-label="Repeat Every">
    <h2 class="dialog-title abs">Repeat Every</h2>
    <div class="dialog-divider abs" style="top:76px"></div>
    <div class="option abs" style="top:110px"><span class="radio is-checked"></span><span class="option-label">Day</span></div>
    <div class="option abs" style="top:172px"><span class="radio"></span><span class="option-label">Week</span></div>
    <div class="option abs" style="top:234px"><span class="radio"></span><span class="option-label">Month</span></div>
    <div class="option abs" style="top:297px"><span class="radio"></span><span class="option-label">Personalize..</span></div>
    <div class="dialog-divider abs" style="top:366px"></div>
    <span class="dialog-action abs" style="left:267px">CANCEL</span>
    <span class="dialog-action abs" style="left:395px">OK</span>
  </section>
</body>
</html>
```